Business Cards for a law firm

Business cards for our law firm. Use our silhoette logo and OAK COUNSEL - check our website (www.oakcounsel.com)

Contact Information for Business Card

our silhouette logo, OAK COUNSEL, 800-555-0147, Dariel Montague, dariel@oakcounsel.com

Requirements
Must have
• our silhouette logo, OAK COUNSEL, 800-555-0147, Dariel Montague, dariel@oakcounsel.com

```html
<!DOCTYPE html>
<html lang="en">
<head>
<meta charset="UTF-8">
<title>Oak Counsel – Business Cards</title>
<link rel="stylesheet" href="https://fonts.googleapis.com/css2?family=Cinzel:wght@500;700&display=swap">
<style>
  :root {
    --backdrop: #d3d4d6;
    --navy: #233066;
    --navy-light: #293a7a;
    --ink: #1f2d63;
    --paper: #ffffff;
    --figure-tone: #26356f;
  }
  * { margin: 0; padding: 0; box-sizing: border-box; }
  html, body {
    width: 900px; height: 1200px; overflow: hidden;
    background: var(--backdrop);
    font-family: "Cinzel", serif;
  }
  .canvas { position: relative; width: 900px; height: 1200px; }
  .card {
    position: absolute; left: 134px; width: 632px; height: 364px;
  }
  .card--front {
    top: 210px;
    background: linear-gradient(120deg, var(--navy) 0%, var(--navy-light) 100%);
    color: var(--paper);
  }
  .card--back { top: 624px; background: var(--paper); color: var(--ink); }

  .front-brand {
    position: absolute; left: 60px; top: 120px;
    display: flex; align-items: center; gap: 18px;
  }
  .front-brand__mark { width: 26px; height: 26px; background: var(--paper); }
  .front-brand__name {
    font-weight: 700; font-size: 46px; letter-spacing: 1px; line-height: 1;
  }
  .front-url {
    position: absolute; left: 0; right: 0; top: 318px; text-align: center;
    font-weight: 700; font-size: 12px; letter-spacing: 3.5px;
  }

  .back-brand {
    position: absolute; left: 39px; top: 46px;
    font-weight: 700; font-size: 31px; letter-spacing: 0.5px; line-height: 1;
  }
  .person {
    position: absolute; left: 39px; top: 182px;
  }
  .person__name { font-weight: 700; font-size: 25px; line-height: 1; letter-spacing: 0.3px; }
  .person__title { font-weight: 500; font-size: 14px; margin-top: 8px; letter-spacing: 0.5px; }
  .contact { list-style: none; margin-top: 16px; }
  .contact__item {
    display: flex; align-items: center; gap: 5px;
    font-weight: 500; font-size: 12.5px; height: 26px; letter-spacing: 0.3px;
  }
  .contact__item--phone { font-size: 15px; letter-spacing: 2px; }
  .contact__icon { width: 14px; height: 14px; fill: var(--ink); flex: none; }
  .figure-area {
    position: absolute; left: 415px; top: 49px; width: 180px; height: 268px;
    background: linear-gradient(180deg, var(--figure-tone), var(--navy));
    opacity: 0.9;
  }
</style>
</head>
<body>
<main class="canvas">
  <section class="card card--front">
    <div class="front-brand">
      <span class="front-brand__mark"></span>
      <span class="front-brand__name">OAK COUNSEL</span>
    </div>
    <p class="front-url">WWW.OAKCOUNSEL.COM</p>
  </section>

  <section class="card card--back">
    <p class="back-brand">OAK COUNSEL</p>
    <div class="person">
      <p class="person__name">DARIEL MONTAGUE</p>
      <p class="person__title">ATTORNEY</p>
      <ul class="contact">
        <li class="contact__item contact__item--phone">
          <svg class="contact__icon" viewBox="0 0 24 24"><path d="M6.6 10.8a15.2 15.2 0 0 0 6.6 6.6l2.2-2.2a1 1 0 0 1 1-.25 11.4 11.4 0 0 0 3.6.57 1 1 0 0 1 1 1V20a1 1 0 0 1-1 1A17 17 0 0 1 3 4a1 1 0 0 1 1-1h3.5a1 1 0 0 1 1 1c0 1.25.2 2.45.57 3.6a1 1 0 0 1-.25 1z"/></svg>
          800-555-0147
        </li>
        <li class="contact__item">
          <svg class="contact__icon" viewBox="0 0 24 24"><path d="M2 5h20v14H2z M2 5l10 8 10-8" fill="none" stroke="#1f2d63" stroke-width="2"/><path d="M2 5h20l-10 8z"/></svg>
          DARIEL@OAKCOUNSEL.COM
        </li>
        <li class="contact__item">
          <svg class="contact__icon" viewBox="0 0 24 24"><g fill="none" stroke="#1f2d63" stroke-width="2"><circle cx="12" cy="12" r="10"/><ellipse cx="12" cy="12" rx="4" ry="10"/><path d="M2 12h20M4 7h16M4 17h16"/></g></svg>
          WWW.OAKCOUNSEL.COM
        </li>
      </ul>
    </div>
    <div class="figure-area" role="img" aria-label="Large brand silhouette artwork area"></div>
  </section>
</main>
</body>
</html>
```